Super-fantastic-interesting infographic of terribly boring content

-Looking to provide a visually engaging snapshot of the average Canadian investor.
-Help people compare their personal financial situation against the infographic (Average).
-We want viewers to feel engaged and interested in the info presented, not confused and irritated.

Data points to present:

The average Canadian snapshot:
* Average Canadian household Income in 2016: $76,900
* Median Net Worth of Canadian families in 2016: $295,100
* Average annual household expenditures on goods a& services: $62,183
* Median value in principal residence: $349,000
* Highest net annual savings amount (Age 35-44): $10,120
* Number of Canadian families holding a mortgage: 38.4%
* Median Mortgage value of Principal residence: $190,000
* Debt to disposable income ratio average: 172.1
* Total value of all assets held by Canadians in 2016: 12 Trillion dollars
* The principal residence was the single largest asset held (of the 12 Trillion): 32%
* Private pensions was the 2nd largest grouping of assets at 29.2%
* The average borrowing rate for Canadian mortgages: 2.94%
* 74% were fixed rate, 21% were variable and 5% blended.
* 48% of Canadians do not save or invest at all
* 54% of Canadians do not budget regularly
* 1 in 3 Canadians have lost at least 20% in one year
* 51% of Canadians took NO ACTION after losing at least 20% in one year.
* 22% of those people either, hired or fired an advisor

Financial advice landscape:
* # of households in Canada: 13,300,000
* Households with an advisor 5,300,000
* % of households dissatisfied with existing advisor 1,100,000

Target Market(s)

Investors, ages 22-55

Industry/Entity Type

Financial

Font styles to use
Sans Serif

Colors

Designer to choose colors to be used in the design.

Requirements
Must have
• Header: Financial landscape of the average Canadian
Nice to have
• There is a lot of numbers and percentages, find a way to deliver the info using a mix of images, numbers, pictures etc.

```html
<!DOCTYPE html>
<html lang="en">
<head>
<meta charset="utf-8">
<title>Financial Landscape of the Average Canadian</title>
<link href="https://fonts.googleapis.com/css2?family=Oswald:wght@400;500&family=Open+Sans:wght@400;700&display=swap" rel="stylesheet">
<style>
:root{
  --bg:#ffffff;
  --header:#e8e8eb;
  --red:#d4232c;
  --ink:#2b2738;
  --plum:#4b4258;
  --slate:#3c3a52;
  --navy:#2a2947;
  --gold:#f7b02c;
  --green:#3db54a;
  --lime:#d4df26;
  --blue:#1f9ad6;
  --blue-deep:#1b5fa8;
  --white:#ffffff;
}
*{margin:0;padding:0;box-sizing:border-box}
html,body{width:1200px;height:1200px;overflow:hidden;background:var(--bg)}
.canvas{position:relative;width:1200px;height:1200px;overflow:hidden}
.sheet{position:absolute;left:399px;top:0;width:470px;height:1405px;transform:scale(0.854);transform-origin:0 0;font-family:"Open Sans",sans-serif;color:var(--white);overflow:hidden}
.band{position:absolute;left:0;width:470px}
.band--header{top:0;height:130px;background:var(--header)}
.band--snapshot{top:0;height:545px;background:var(--plum)}
.band--assets{top:545px;height:453px;background:var(--slate)}
.band--losses{top:998px;height:408px;background:var(--navy)}
.abs{position:absolute}
.art{position:absolute;border-radius:4px}
.num{font-family:"Oswald",sans-serif;font-weight:500;color:var(--gold);line-height:1;letter-spacing:-0.5px}
.cap{font-size:9px;line-height:10px;text-align:center;color:var(--white)}
.cap b{font-weight:700}
.stat{position:absolute;text-align:center}
.title-main{font-family:"Oswald",sans-serif;font-weight:500;color:var(--red);font-size:31px;line-height:1;letter-spacing:-0.5px}
.title-sub{font-family:"Oswald",sans-serif;font-weight:400;color:var(--ink);font-size:20px;line-height:1;margin-top:4px}
.meter{position:absolute;height:14px;border-radius:7px;background:var(--white);overflow:hidden}
.meter span{display:block;height:100%;border-radius:7px}
.pair{position:absolute;display:flex;align-items:center;gap:6px}
.big-note{font-size:13px;line-height:13px;color:var(--white);white-space:nowrap}
.big-note b{font-weight:700}
.ribbon{position:absolute;left:210px;top:1162px;width:232px;height:26px}
.ribbon-text{position:absolute;left:210px;top:1162px;width:232px;height:26px;text-align:center;font-family:"Oswald",sans-serif;color:var(--navy);font-size:18px;line-height:26px;letter-spacing:-0.5px}
.tree-item{position:absolute;font-size:10px;line-height:10px;color:var(--white)}
.tree-item .num{font-size:20px;display:block;margin-top:2px}
</style>
</head>
<body>
<div class="canvas">
<div class="sheet">
  <div class="band band--snapshot"></div>
  <div class="band band--header"></div>
  <svg class="abs" style="left:0;top:60px" width="470" height="140" viewBox="0 0 470 140">
    <polygon points="0,80 470,60 470,120 0,140" fill="var(--plum)"/>
    <polygon points="300,70 470,60 470,122 400,100" fill="var(--red)"/>
    <polygon points="0,76 470,56 470,62 0,82" fill="#c9c8cf"/>
  </svg>
  <div class="band band--assets"></div>
  <div class="band band--losses"></div>

  <!-- Header -->
  <div class="art" role="img" aria-label="Canadian flag on a pole" style="left:48px;top:18px;width:105px;height:66px;background:linear-gradient(90deg,var(--red) 25%,#fff 25%,#fff 75%,var(--red) 75%)"></div>
  <div class="abs" style="left:180px;top:25px">
    <div class="title-main">FINANCIAL LANDSCAPE</div>
    <div class="title-sub">OF THE AVERAGE CANADIAN</div>
  </div>
  <div class="art" role="img" aria-label="Map of Canada" style="left:20px;top:105px;width:175px;height:125px;background:linear-gradient(160deg,#ffffff,#cfe1f3);border-radius:30px 60px 20px 40px"></div>

  <div class="art" role="img" aria-label="House, earner and money bag icons" style="left:205px;top:160px;width:112px;height:50px;background:linear-gradient(90deg,#fff 0 35%,var(--gold) 35% 60%,var(--green) 60%)"></div>
  <div class="num abs" style="left:325px;top:172px;font-size:38px">$76,900</div>
  <div class="abs" style="left:205px;top:218px;font-size:10px;color:var(--white)">Average Canadian household <b>Income in <span style="color:var(--gold)">2016</span></b></div>

  <!-- Row 1 -->
  <div class="art" role="img" aria-label="Stack of coins with rising green chart" style="left:28px;top:245px;width:105px;height:72px;background:linear-gradient(135deg,#fff 0 45%,var(--green) 45%)"></div>
  <div class="abs" style="left:86px;top:222px;font-family:Oswald,sans-serif;font-size:17px;line-height:1">2016</div>
  <div class="art" role="img" aria-label="Shopping cart and serving cloche on a hand" style="left:175px;top:262px;width:120px;height:55px;background:linear-gradient(90deg,#fff 0 55%,var(--green) 55%)"></div>
  <div class="art" role="img" aria-label="Residential building" style="left:355px;top:265px;width:62px;height:52px;background:linear-gradient(180deg,#fff 0 60%,var(--green) 60%)"></div>

  <div class="stat" style="left:10px;top:322px;width:150px"><div class="cap"><b>Median Net Worth</b><br>of Canadian families</div><div class="num" style="font-size:32px;margin-top:4px">$295,100</div></div>
  <div class="stat" style="left:160px;top:322px;width:155px"><div class="cap">Average annual household<br>expenditures on <b>goods &amp; services</b></div><div class="num" style="font-size:32px;margin-top:4px">$62,183</div></div>
  <div class="stat" style="left:315px;top:322px;width:140px"><div class="cap">Median value in<br><b>principal residence</b></div><div class="num" style="font-size:32px;margin-top:4px">$349,000</div></div>

  <!-- Row 2 -->
  <div class="art" role="img" aria-label="Piggy bank with coin" style="left:38px;top:400px;width:60px;height:62px;background:#fff"></div>
  <div class="art" role="img" aria-label="Person aged 35 to 44" style="left:108px;top:420px;width:16px;height:42px;background:var(--gold)"></div>
  <div class="abs" style="left:100px;top:402px;font-size:8px;font-weight:700">Age 35-44</div>
  <div class="art" role="img" aria-label="House with money bag and approved stamp" style="left:168px;top:402px;width:62px;height:58px;background:linear-gradient(180deg,#fff 0 50%,var(--gold) 50%)"></div>
  <svg class="abs" style="left:234px;top:405px" width="58" height="58" viewBox="0 0 58 58"><circle cx="29" cy="29" r="28" fill="var(--white)"/><circle cx="29" cy="29" r="25" fill="var(--green)"/><path d="M29 29 L29 4 A25 25 0 0 0 6 39 Z" fill="var(--white)"/><text x="34" y="22" font-family="Oswald" font-size="7" fill="var(--white)">38.4%</text></svg>
  <div class="art" role="img" aria-label="Building, hand and approval stamp" style="left:345px;top:400px;width:95px;height:60px;background:linear-gradient(90deg,#fff 0 45%,var(--green) 45% 75%,#e7e7ea 75%)"></div>

  <div class="stat" style="left:10px;top:465px;width:150px"><div class="cap">Highest net annual<br><b>savings amount</b></div><div class="num" style="font-size:32px;margin-top:4px">$10,120</div></div>
  <div class="stat" style="left:160px;top:465px;width:155px"><div class="cap">Number of Canadian families<br><b>holding a mortgage</b></div><div class="num" style="font-size:32px;margin-top:4px">38.4%</div></div>
  <div class="stat" style="left:315px;top:465px;width:140px"><div class="cap"><b>Median Mortgage value</b><br>of Principal residence</div><div class="num" style="font-size:32px;margin-top:4px">$190,000</div></div>

  <!-- Assets band -->
  <div class="art" role="img" aria-label="Person carrying a heavy debt bag" style="left:32px;top:563px;width:80px;height:82px;background:linear-gradient(135deg,var(--green) 0 45%,#fff 45%)"></div>
  <div class="stat" style="left:5px;top:648px;width:140px"><div class="cap"><b>Debt to disposable<br>income</b> ratio average</div><div class="num" style="font-size:31px;margin-top:6px">172.1</div></div>

  <svg class="abs" style="left:137px;top:562px" width="205" height="80" viewBox="0 0 205 80">
    <circle cx="38" cy="38" r="36" fill="var(--white)"/>
    <path d="M38 38 L38 4 A34 34 0 0 0 8.6 55 Z" fill="#8dc63f"/>
    <path d="M38 38 L38 4 A34 34 0 0 1 67.4 55 Z" fill="var(--green)"/>
    <path d="M38 38 L67.4 55 A34 34 0 0 1 8.6 55 Z" fill="#1f8a3a"/>
    <text x="14" y="38" font-family="Oswald" font-size="20" fill="#fff">$</text>
    <rect x="46" y="22" width="14" height="12" fill="#fff"/>
    <rect x="28" y="54" width="20" height="8" rx="3" fill="#fff"/>
    <text x="160" y="22" font-family="Oswald" font-size="17" fill="var(--gold)">2016</text>
    <line x1="82" y1="76" x2="200" y2="76" stroke="#fff" stroke-width="1"/>
    <polyline points="84,68 94,45 104,60 115,46 125,62 136,44 146,58 156,40 167,54 177,36 188,48 198,26" fill="none" stroke="var(--gold)" stroke-width="1.5"/>
    <polyline points="84,72 94,56 104,70 115,58 125,68 136,55 146,66 156,52 167,63 177,48 188,58 198,34" fill="none" stroke="var(--red)" stroke-width="1.5"/>
  </svg>
  <div class="abs" style="left:142px;top:650px;font-size:9px;font-weight:700;white-space:nowrap">Total value of all assets held by Canadians</div>
  <div class="num abs" style="left:138px;top:668px;font-size:29px;letter-spacing:-1px;white-space:nowrap">12 Trillion dollars</div>

  <svg class="abs" style="left:345px;top:570px" width="120" height="80" viewBox="0 0 120 80">
    <circle cx="36" cy="38" r="35" fill="var(--green)"/>
    <path d="M36 38 L36 3 A35 35 0 0 0 2 46 Z" fill="#fff"/>
    <rect x="16" y="22" width="16" height="18" fill="var(--slate)"/>
    <path d="M70 15 Q92 18 96 40" fill="none" stroke="#fff" stroke-width="3"/>
    <polygon points="89,38 103,38 96,48" fill="#fff"/>
    <text x="74" y="74" font-family="Oswald" font-size="22" fill="#fff">32%</text>
  </svg>
  <div class="abs" style="left:357px;top:654px;font-size:8px;line-height:9px">The principal residence<br>was the <b>single largest<br>asset held</b><br>(of the 12 Trillion):</div>

  <div class="art" role="img" aria-label="Couple figures with a dollar sign" style="left:45px;top:715px;width:60px;height:60px;background:linear-gradient(90deg,#8dc63f 0 50%,var(--green) 50%)"></div>
  <div class="stat" style="left:5px;top:780px;width:140px"><div class="cap"><b>Private pensions</b><br>was the 2nd largest<br>grouping of assets at</div><div class="num" style="font-size:31px;margin-top:4px">29.2%</div></div>

  <div class="art" role="img" aria-label="Hand holding a money bag" style="left:148px;top:735px;width:45px;height:72px;background:#fff"></div>
  <div class="art" role="img" aria-label="Open receiving hand" style="left:222px;top:778px;width:55px;height:28px;background:var(--green)"></div>
  <div class="abs" style="left:202px;top:728px;font-size:9px;line-height:10px">The average<br><b>borrowing rate</b><br>for Canadian<br>mortgages</div>
  <div class="num abs" style="left:185px;top:815px;font-size:31px">2.94%</div>

  <svg class="abs" style="left:285px;top:720px" width="160" height="120" viewBox="0 0 160 120">
    <line x1="4" y1="0" x2="4" y2="100" stroke="#fff" stroke-width="1.5"/>
    <line x1="4" y1="100" x2="156" y2="100" stroke="#fff" stroke-width="1.5"/>
    <rect x="22" y="25" width="25" height="75" fill="var(--blue)"/>
    <rect x="58" y="78" width="25" height="22" fill="var(--blue-deep)"/>
    <rect x="94" y="90" width="25" height="10" fill="#2c3e8c"/>
    <text x="22" y="20" font-family="Oswald" font-size="19" fill="#fff">74%</text>
    <text x="58" y="73" font-family="Oswald" font-size="19" fill="#fff">21%</text>
    <text x="94" y="85" font-family="Oswald" font-size="19" fill="#fff">5 %</text>
    <text x="22" y="116" font-family="Oswald" font-size="8" fill="#fff">FIX RATE</text>
    <text x="57" y="116" font-family="Oswald" font-size="8" fill="#fff">VARIABLE</text>
    <text x="93" y="116" font-family="Oswald" font-size="8" fill="#fff">BLENDED</text>
  </svg>

  <div class="art" role="img" aria-label="Person with shopping bag" style="left:60px;top:875px;width:40px;height:32px;background:var(--gold)"></div>
  <div class="art" role="img" aria-label="Investor with chart" style="left:165px;top:875px;width:35px;height:32px;background:#fff"></div>
  <div class="meter" style="left:35px;top:912px;width:184px"><span style="width:52%;background:var(--lime)"></span></div>
  <div class="pair" style="left:38px;top:934px">
    <div class="num" style="font-size:44px;color:var(--lime)">48%</div>
    <div class="big-note">of Canadians<br><b>do not save<br>or invest at all</b></div>
  </div>

  <div class="art" role="img" aria-label="Banknotes with exchange arrows" style="left:268px;top:865px;width:65px;height:40px;background:linear-gradient(90deg,var(--green),var(--gold))"></div>
  <div class="art" role="img" aria-label="Calculator and budget sheet" style="left:368px;top:865px;width:68px;height:42px;background:linear-gradient(90deg,#fff 0 55%,var(--lime) 55%)"></div>
  <div class="meter" style="left:256px;top:912px;width:185px"><span style="width:58%;background:var(--green)"></span></div>
  <div class="pair" style="left:262px;top:934px">
    <div class="num" style="font-size:44px;color:var(--green)">54%</div>
    <div class="big-note">of Canadians<br><b>do not budget<br>regularly</b></div>
  </div>

  <!-- Losses band -->
  <div class="art" role="img" aria-label="Three people, one highlighted" style="left:38px;top:1018px;width:68px;height:75px;background:linear-gradient(90deg,#fff 0 35%,var(--gold) 35% 65%,#fff 65%)"></div>
  <div class="abs" style="left:115px;top:1025px;line-height:1">
    <div style="font-size:12px">1 in 3 Canadians</div>
    <div style="font-size:22px;margin-top:2px">have lost</div>
    <div style="font-size:22px">at least</div>
  </div>
  <div class="pair" style="left:224px;top:1016px;gap:8px;align-items:flex-start">
    <div class="num" style="font-size:72px;color:var(--blue)">20%</div>
    <div style="font-size:22px;font-weight:700;line-height:23px;margin-top:4px;white-space:nowrap">in<br>one year</div>
  </div>
  <div class="art" role="img" aria-label="Small group of three people" style="left:128px;top:1100px;width:42px;height:45px;background:linear-gradient(90deg,#fff 0 33%,var(--gold) 33% 66%,#fff 66%)"></div>
  <svg class="abs" style="left:55px;top:1100px" width="30" height="60" viewBox="0 0 30 60"><rect x="11" y="0" width="8" height="42" fill="var(--gold)"/><polygon points="0,38 30,38 15,58" fill="var(--gold)"/></svg>
  <svg class="abs" style="left:145px;top:1120px" width="90" height="60" viewBox="0 0 90 60"><line x1="0" y1="55" x2="83" y2="12" stroke="var(--gold)" stroke-width="1"/><circle cx="84" cy="11" r="2.5" fill="var(--gold)"/></svg>
  <div class="pair" style="left:228px;top:1108px;gap:5px">
    <div class="num" style="font-size:34px">22%</div>
    <div style="font-size:9.5px;line-height:10px;white-space:nowrap">of those people<br><b>either, hired<br>or fired an advisor</b></div>
  </div>
  <div class="art" role="img" aria-label="People meeting around a table" style="left:395px;top:1098px;width:50px;height:46px;background:#fff"></div>

  <div class="num abs" style="left:34px;top:1178px;font-size:68px;color:var(--blue)">51%</div>
  <div class="abs" style="left:28px;top:1258px;width:130px;text-align:center;line-height:1">
    <div style="font-size:11px">of Canadians took</div>
    <div style="font-family:Oswald,sans-serif;font-size:27px;margin:2px 0">NO ACTION</div>
    <div style="font-size:11px">after losing at least<br>20% in one year.</div>
  </div>
  <div class="art" role="img" aria-label="Confused man with a scribble above his head" style="left:165px;top:1195px;width:62px;height:150px;background:linear-gradient(180deg,#cfd0de 0 20%,#fff 20%);border-radius:30px 30px 6px 6px"></div>

  <svg class="ribbon" viewBox="0 0 232 26"><polygon points="0,0 232,0 222,13 232,26 0,26 10,13" fill="var(--blue)"/></svg>
  <div class="ribbon-text">Financial advice landscape</div>

  <svg class="abs" style="left:235px;top:1188px" width="40" height="150" viewBox="0 0 40 150"><path d="M5 0 V145 H35 M12 0 V90 H35 M19 0 V35 H35" fill="none" stroke="var(--gold)" stroke-width="1"/></svg>
  <div class="art" role="img" aria-label="House with family" style="left:262px;top:1210px;width:32px;height:28px;background:#fff"></div>
  <div class="tree-item" style="left:300px;top:1198px">
    # of households<br>in Canada:<span class="num">13,300,000</span>
  </div>
  <div class="art" role="img" aria-label="House with tick" style="left:308px;top:1260px;width:32px;height:28px;background:#fff"></div>
  <div class="tree-item" style="left:350px;top:1255px">
    Households<br>with an advisor<span class="num">5,300,000</span>
  </div>
  <div class="art" role="img" aria-label="Thumbs down" style="left:262px;top:1312px;width:28px;height:30px;background:#fff"></div>
  <div class="tree-item" style="left:300px;top:1310px">
    % of households dissatisfied<br>with existing advisor<span class="num">1,100,000</span>
  </div>
</div>
</div>
</body>
</html>
```